GPS SALES

Lopoking to design a website for my company " Pendry Fabrications"
Our slogan is "GPS that's made to fit"

I sell in dash gps systems for cars that are built into the dash board. No gaps after install. designed specifically for specific cars.
I have products for all manufacturers...

Want lots of colour!
Online ordering system with payment options online

This is a sales only website....

A site that sells similar products is:
http://e.velmotrax.cn/
I want my website to be very similar to this one.

Im basically selling these products here in australia. So I really want something "australian themed" (kangaroo or koala or australia map....)this kind of thing

Looking to attract business from car dealerships and the public.

I have attached a copy of my brochure, and some of the products I sell

Gps

```html
<!DOCTYPE html>
<html lang="en">
<head>
<meta charset="utf-8">
<title>Pendry Fabrications — GPS that's made to fit</title>
<link href="https://fonts.googleapis.com/css2?family=Merriweather:wght@400;700&family=Open+Sans:wght@300;400;600;700&display=swap" rel="stylesheet">
<style>
:root{
  --blue:#1d5ba6;
  --blue-dark:#174d8f;
  --orange:#e8683a;
  --orange-text:#e8642a;
  --text:#555;
  --muted:#888;
  --white:#fff;
  --rule:#ccc;
}
*{box-sizing:border-box;margin:0;padding:0}
html,body{width:1140px;height:1200px;overflow:hidden;background:var(--white)}
body{position:relative;font-family:'Open Sans',sans-serif;color:var(--text)}
.abs{position:absolute}

/* header */
.brand{left:168px;top:10px;display:flex;align-items:center;gap:8px}
.brand-mark{width:30px;height:30px;background:var(--blue);border-radius:4px}
.brand-name{font-family:'Open Sans',sans-serif;font-weight:700;font-size:24px;line-height:1;color:var(--blue)}
.tagline{left:168px;top:60px;font-size:15px;font-weight:600;color:#222}
.social{top:15px;width:27px;height:27px;border-radius:50%;background:var(--blue)}
.nav{top:50px;left:468px;display:flex;height:31px}
.nav a{display:block;height:31px;line-height:31px;font-size:14px;font-weight:600;color:#444;text-decoration:none;padding:0 25px;border-right:1px solid var(--rule)}
.nav a:last-child{border-right:none}
.nav a.active{background:var(--blue);color:var(--white);padding:0 15px;border-right:none}
.header-bar{left:0;top:81px;width:1140px;height:9px;background:var(--blue)}

/* hero */
.hero{left:0;top:90px;width:1140px;height:418px;background:linear-gradient(90deg,#e0602f,#ec6e3f 50%,#e0602f)}
.hero-title{left:176px;top:158px;font-family:'Merriweather',serif;font-weight:400;font-size:44px;line-height:49px;color:var(--white)}
.hero-text{left:176px;top:268px;width:360px;font-size:15px;line-height:23.5px;font-weight:600;color:var(--white)}
.btn{display:block;background:var(--blue);color:var(--white);font-family:'Merriweather',serif;text-align:center;text-decoration:none;box-shadow:0 2px 3px rgba(0,0,0,.3)}
.hero-btn{left:179px;top:364px;width:148px;height:43px;line-height:43px;font-size:16px}
.hero-device{left:540px;top:138px;width:420px;height:306px;background:linear-gradient(180deg,#3a3a3a,#1c1c1c);border-radius:14px}
.hero-arrow{top:255px;width:72px;height:72px;border-radius:50%;background:rgba(255,255,255,.3)}
.dot{top:477px;width:14px;height:14px;border-radius:50%;border:2px solid var(--white);background:var(--blue)}
.dot.on{background:var(--orange)}

/* columns */
.col-title{top:550px;font-family:'Merriweather',serif;font-weight:700;font-size:21px;color:var(--blue)}
.col-photo{top:586px;width:260px;height:144px}
.col-text{top:735px;width:260px;font-size:12px;line-height:18.5px;font-weight:300;color:#444}
.more{color:var(--orange-text);font-style:italic;font-size:11px;text-decoration:underline;margin-left:6px}
.quote{left:731px;top:594px;width:240px;font-size:13.5px;line-height:21px;font-weight:300;color:#444;text-indent:42px}
.quote-mark{left:730px;top:578px;font-family:'Merriweather',serif;font-weight:700;font-size:48px;color:var(--orange-text);line-height:1}
.author{left:729px;top:752px;font-size:13px;font-weight:600;color:var(--orange-text)}
.author-loc{left:730px;top:770px;font-size:9.5px;color:var(--muted)}

/* welcome */
.welcome-photo{left:138px;top:842px;width:369px;height:248px;background:linear-gradient(160deg,#5b5d61,#2a2b2e);border-radius:12px}
.welcome-title{left:546px;top:838px;font-family:'Merriweather',serif;font-weight:700;font-size:28px;color:var(--blue)}
.welcome-text{left:543px;width:430px;font-size:13.5px;line-height:21px;font-weight:300;color:#444}
.welcome-btn{left:545px;top:1033px;width:115px;height:32px;line-height:32px;font-size:14px}

/* footer */
.footer{left:0;top:1151px;width:1140px;height:49px;background:var(--blue);border-top:3px solid var(--blue-dark)}
.copy{left:159px;top:1167px;font-size:13px;color:var(--white)}
.foot-link{top:1168px;font-size:12px;color:#dce6f4}
</style>
</head>
<body>

<header>
  <div class="abs brand"><span class="brand-mark"></span><span class="brand-name">Pendry Fabrications</span></div>
  <div class="abs tagline">GPS thats made to fit!</div>
  <span class="abs social" style="left:900px" aria-label="Social link"></span>
  <span class="abs social" style="left:936px" aria-label="Social link"></span>
  <nav class="abs nav">
    <a class="active" href="#">Home</a>
    <a href="#">Services</a>
    <a href="#">Products</a>
    <a href="#">About Us</a>
    <a href="#">Contact Us</a>
  </nav>
  <div class="abs header-bar"></div>
</header>

<section>
  <div class="abs hero" role="img" aria-label="Orange backdrop of car manufacturer emblems"></div>
  <h1 class="abs hero-title">Dash GPS<br>Systems for cars</h1>
  <p class="abs hero-text">Selling in dash gps systems for cars that are built into the dash board. No gaps after install. designed specifically for specific cars.</p>
  <a class="abs btn hero-btn" href="#">Shop Now</a>
  <div class="abs hero-device" role="img" aria-label="In-dash GPS head unit showing a navigation map"></div>
  <div class="abs hero-arrow" style="left:24px">
    <svg width="72" height="72"><polyline points="42,20 26,36 42,52" fill="none" stroke="rgba(255,255,255,.6)" stroke-width="5"/></svg>
  </div>
  <div class="abs hero-arrow" style="left:1042px">
    <svg width="72" height="72"><polyline points="30,20 46,36 30,52" fill="none" stroke="rgba(255,255,255,.6)" stroke-width="5"/></svg>
  </div>
  <span class="abs dot" style="left:530px"></span>
  <span class="abs dot on" style="left:551px"></span>
  <span class="abs dot" style="left:573px"></span>
  <span class="abs dot" style="left:596px"></span>
</section>

<section>
  <h2 class="abs col-title" style="left:170px">Our Products</h2>
  <div class="abs col-photo" style="left:168px;background:linear-gradient(180deg,#6d5a4a,#2e2a28)" role="img" aria-label="Car dashboard with an installed GPS unit"></div>
  <p class="abs col-text" style="left:169px">Our products are designed specifically for specific cars with a wide range of car model and manufacturers <a class="more" href="#">learn more &gt;</a></p>

  <h2 class="abs col-title" style="left:443px">Services</h2>
  <div class="abs col-photo" style="left:440px;background:linear-gradient(135deg,#2a2a2a,#9a9a9a)" role="img" aria-label="Technician with a laptop working inside a car"></div>
  <p class="abs col-text" style="left:440px">Sed ut perspiciatis unde omnis iste natus error sit voluptatem each&nbsp; sa quae ab illo inventore veritatis et <a class="more" href="#">learn more &gt;</a></p>

  <h2 class="abs col-title" style="left:731px">Testimonials</h2>
  <span class="abs quote-mark">&#8220;</span>
  <p class="abs quote">Aspernatur aut dit aut fugit sedy quia consequtur magnifest doluptatem sequi nesciunt Neque porro quisquam est, qui dolorem ipsum quia. Tus amen lorem ipsum dolore ang bantot modist tempora incidunt ut labore dolore ist magnam aliquaat voluptatem.</p>
  <div class="abs author">John Doe Smith</div>
  <div class="abs author-loc">Perth, Western Australia</div>
</section>

<section>
  <div class="abs welcome-photo" role="img" aria-label="Three in-dash GPS units displaying maps"></div>
  <h2 class="abs welcome-title">Welcome to Pendry Fabrications</h2>
  <p class="abs welcome-text" style="top:887px">Sed ut perspiciatis unde omnis iste natus error sit voluptatem each&nbsp; sa quae ab illo inventore veritatis et quasi architecto bea tae vitae dictarts explicabo. Nemo enim ipsam voluptatem quia volup tas sit.</p>
  <p class="abs welcome-text" style="top:959px">Aspernatur aut odit aut fugit sed quia consequuntur magni doluptatem sequi nesciunt Neque porro quisquam est, qui dolorem ipsum quia.</p>
  <a class="abs btn welcome-btn" href="#">Learn More</a>
</section>

<footer>
  <div class="abs footer"></div>
  <div class="abs copy">Copyright Pendry Fabrications . All right reserved.</div>
  <span class="abs foot-link" style="left:553px">Home</span>
  <span class="abs foot-link" style="left:624px">Services</span>
  <span class="abs foot-link" style="left:717px">Products</span>
  <span class="abs foot-link" style="left:814px">About Us</span>
  <span class="abs foot-link" style="left:910px">Contact Us</span>
</footer>

</body>
</html>
```